Visual consulting framework

Thornwell Advisory is a financial consulting business that takes it clients on the following journey:
1. Get fit (disciplined)
2. Get funded (access to capital)
3. Get big (grow)
4. Get out (exit with wealth)
Over thirty years we have identified that the key to being successful on this journey are the following elements or components.
1. Vision
2. Strategy
3. Structure
4. Product & services
5. Sales and marketing
6. System and processes
7. People
8. Culture
9. Finance
10. M&A
11. Performance monitoring
12. Risk management
We require a visual representation of these elements and the journey to communicate to clients and prospects in marketing material.
Look and feel
Each slider illustrates characteristics of the customer's brand and the style your logo design should communicate.

```html
<!DOCTYPE html>
<html lang="en">
<head>
<meta charset="utf-8">
<title>Thornwell Advisory – Consulting Framework</title>
<link href="https://fonts.googleapis.com/css2?family=Ubuntu:ital,wght@0,500;0,700;1,700&display=swap" rel="stylesheet">
<style>
  :root{
    --page:#e6e6e6;
    --panel-top:#f4efec;
    --panel-bottom:#f7f1ef;
    --orange:#f7931e;
    --blue:#0f9ae0;
    --blue-text:#1a8fd8;
    --peach:#fde9d6;
    --band:#ffffff;
    --band-grey:#d9d9d9;
    --white:#ffffff;
  }
  *{box-sizing:border-box;margin:0;padding:0}
  html,body{width:1200px;height:720px;overflow:hidden}
  body{background:var(--page);font-family:"Ubuntu",sans-serif;position:relative}
  .panel{position:absolute;left:67px;top:61px;width:1065px;height:598px;
    background:linear-gradient(180deg,var(--panel-top),var(--panel-bottom))}
  .band{position:absolute;height:26px;background:var(--band-grey);opacity:.55}
  .band--light{background:var(--band);opacity:.8}
  .pill{position:absolute;width:166px;height:75px;border-radius:38px;display:flex;
    align-items:center;justify-content:center;text-align:center;font-weight:700;
    font-size:17px;line-height:20px;color:var(--white);background:var(--orange)}
  .pill--italic{font-style:italic}
  .pill--outline{background:var(--white);border:2px solid var(--blue);color:var(--blue-text)}
  .pill--soft{background:var(--peach);border:1.5px solid var(--orange);color:var(--blue-text);width:164px;height:73px}
  .stage{position:absolute;width:172px;height:73px;display:flex;align-items:center;
    justify-content:center;text-align:center;font-weight:700;font-style:italic;
    font-size:17px;line-height:20px;color:var(--blue-text);padding-left:8px}
  .badge{position:absolute;width:34px;height:34px;border-radius:50%;background:var(--blue);
    border:2px solid var(--white);transform:translate(-50%,-50%)}
  .badge::after{content:"";position:absolute;left:9px;top:9px;width:12px;height:12px;
    border:2px solid var(--white);border-radius:3px}
  .overlay{position:absolute;left:0;top:0}
  .brand{position:absolute;left:110px;top:499px;width:227px;height:101px;border-radius:50px;
    background:var(--white);display:flex;align-items:center;justify-content:center;gap:10px}
  .brand__dot{width:34px;height:34px;border-radius:50%;background:var(--blue)}
  .brand__name{font-weight:500;font-size:19px;line-height:21px;color:var(--orange)}
</style>
</head>
<body>
  <div class="panel" role="img" aria-label="Soft faded photo of a business meeting with charts"></div>

  <div class="band band--light" style="left:313px;top:115px;width:819px"></div>
  <div class="band band--light" style="left:151px;top:407px;width:981px"></div>

  <!-- components, top row -->
  <div class="pill pill--italic" style="left:151px;top:91px">Perfomance<br>Management</div>
  <div class="pill" style="left:347px;top:91px">Vision</div>
  <div class="pill" style="left:526px;top:91px">Strategy</div>
  <div class="pill" style="left:703px;top:91px">Structure</div>
  <div class="pill" style="left:881px;top:91px">Product<br>Services</div>

  <div class="pill pill--outline" style="left:151px;top:241px">Risk<br>Management</div>

  <!-- components, bottom row -->
  <div class="pill pill--italic" style="left:151px;top:383px">Perfomance<br>Management</div>
  <div class="pill" style="left:347px;top:383px">Systems &amp;<br>Processes</div>
  <div class="pill" style="left:526px;top:383px">Finance</div>
  <div class="pill" style="left:703px;top:383px">Sales &amp;<br>Marketing</div>
  <div class="pill" style="left:881px;top:383px">M &amp; A</div>

  <!-- journey outlines -->
  <svg class="overlay" width="1200" height="720" viewBox="0 0 1200 720" aria-hidden="true">
    <g fill="var(--white)">
      <rect x="341" y="189" width="172" height="73" rx="36.5"/>
      <rect x="341" y="285" width="172" height="73" rx="36.5"/>
      <rect x="525" y="189" width="172" height="73" rx="36.5"/>
      <rect x="525" y="285" width="172" height="73" rx="36.5"/>
      <rect x="703" y="189" width="172" height="73" rx="36.5"/>
      <rect x="703" y="285" width="172" height="73" rx="36.5"/>
      <rect x="891" y="189" width="172" height="73" rx="36.5"/>
      <rect x="891" y="285" width="172" height="73" rx="36.5"/>
    </g>
    <g fill="none" stroke="var(--blue)" stroke-width="2.5">
      <path d="M470 189 H476.5 A36.5 36.5 0 0 1 476.5 262 H375"/>
      <path d="M470 285 H476.5 A36.5 36.5 0 0 1 476.5 358 H375"/>
      <path d="M654 189 H660.5 A36.5 36.5 0 0 1 660.5 262 H559"/>
      <path d="M654 285 H660.5 A36.5 36.5 0 0 1 660.5 358 H559"/>
      <path d="M832 189 H838.5 A36.5 36.5 0 0 1 838.5 262 H737"/>
      <path d="M832 285 H838.5 A36.5 36.5 0 0 1 838.5 358 H737"/>
      <path d="M1020 189 H1026.5 A36.5 36.5 0 0 1 1026.5 262 H925"/>
      <path d="M1020 285 H1026.5 A36.5 36.5 0 0 1 1026.5 358 H925"/>
    </g>
    <g fill="var(--blue)">
      <path d="M513 220 l7 5.5 -7 5.5z"/><path d="M513 316 l7 5.5 -7 5.5z"/>
      <path d="M697 220 l7 5.5 -7 5.5z"/><path d="M697 316 l7 5.5 -7 5.5z"/>
      <path d="M875 220 l7 5.5 -7 5.5z"/><path d="M875 316 l7 5.5 -7 5.5z"/>
      <path d="M1063 220 l7 5.5 -7 5.5z"/><path d="M1063 316 l7 5.5 -7 5.5z"/>
    </g>
    <g stroke="var(--blue)" stroke-width="1" stroke-dasharray="2 3">
      <line x1="424" y1="264" x2="424" y2="283"/>
      <line x1="607" y1="264" x2="607" y2="283"/>
      <line x1="790" y1="264" x2="790" y2="283"/>
      <line x1="973" y1="264" x2="973" y2="283"/>
    </g>
    <g fill="var(--white)" stroke="var(--blue)" stroke-width="1.5">
      <circle cx="364" cy="276" r="23"/>
      <circle cx="547" cy="276" r="23"/>
      <circle cx="729" cy="276" r="23"/>
      <circle cx="913" cy="276" r="23"/>
    </g>
    <g fill="none" stroke="var(--blue)" stroke-width="1.5">
      <path d="M355 284 l8 -8 5 4 8 -10"/>
      <path d="M540 270 h14 M547 270 v10 M543 284 h8"/>
      <path d="M720 285 l16 -16 M730 269 h6 v6"/>
      <path d="M905 283 h16 M907 278 h12 M909 273 h8"/>
    </g>
    <!-- people & culture markers -->
    <g fill="none" stroke="var(--blue)" stroke-width="1.5">
      <circle cx="880" cy="510" r="14"/>
      <circle cx="1042" cy="510" r="14"/>
      <circle cx="880" cy="598" r="14"/>
      <circle cx="1042" cy="598" r="14"/>
    </g>
  </svg>

  <div class="stage" style="left:341px;top:189px">Get Fit</div>
  <div class="stage" style="left:341px;top:285px">Discipline</div>
  <div class="stage" style="left:525px;top:189px">Get Funded</div>
  <div class="stage" style="left:525px;top:285px">Access to<br>Capital</div>
  <div class="stage" style="left:703px;top:189px">Get Big</div>
  <div class="stage" style="left:703px;top:285px">Grow</div>
  <div class="stage" style="left:891px;top:189px">Get out</div>
  <div class="stage" style="left:891px;top:285px">Exit with<br>Wealth</div>

  <!-- component badges -->
  <span class="badge" style="left:430px;top:165px"></span>
  <span class="badge" style="left:608px;top:165px"></span>
  <span class="badge" style="left:786px;top:165px"></span>
  <span class="badge" style="left:963px;top:165px"></span>
  <span class="badge" style="left:430px;top:383px"></span>
  <span class="badge" style="left:608px;top:383px"></span>
  <span class="badge" style="left:786px;top:383px"></span>
  <span class="badge" style="left:963px;top:383px"></span>

  <div class="pill pill--soft" style="left:881px;top:475px">People</div>
  <div class="pill pill--soft" style="left:881px;top:561px">Culture</div>

  <div class="brand">
    <span class="brand__dot"></span>
    <span class="brand__name">Thornwell<br>Advisory</span>
  </div>
</body>
</html>
```